Brightwell Pictures Business Card

Hello,

i would like to have a dynamic, creative but tasteful card, colour used, front and back. I have attached a sample card that I liked very much from another individual to give you an idea of the theme/approach, but not colour. Ideally the graphic elements of the Brightwell Logo are brought into the design.

Target Market(s)

North America

Industry/Entity Type

Film Production

Contact Information for Business Card

Mirela Vantasch
President/Founder
Brightwell Pictures Inc.
587 914 3362
mirela@brightwellpix.tv

Font styles to use
Sans Serif

Colors
6b449b
5c5c5c
fdfdfd
000000

Requirements
Must have
• Logo, name, Company name, email and cell number. no Address line to be included.
Should not have
• any unrelated GFX elements, serif fonts

```html
<!DOCTYPE html>
<html lang="en">
<head>
<meta charset="utf-8">
<title>Brightwell Pictures Business Card</title>
<link href="https://fonts.googleapis.com/css2?family=Jost:wght@500;700&display=swap" rel="stylesheet">
<style>
  :root {
    --purple: #6b449b;
    --purple-deep: #4f2488;
    --charcoal: #5c5c5c;
    --paper: #fdfdfd;
    --band-grey: #cfcfcf;
    --backdrop: #e4e4e6;
  }
  * { margin: 0; padding: 0; box-sizing: border-box; }
  html, body { width: 1200px; height: 918px; overflow: hidden; }
  body {
    background: var(--backdrop);
    font-family: "Jost", "Futura", sans-serif;
    position: relative;
  }
  .card {
    position: absolute;
    left: 250px;
    width: 700px;
    height: 400px;
    background: var(--paper);
    overflow: hidden;
    box-shadow: 0 6px 18px rgba(0,0,0,0.18);
  }
  .card--front { top: 40px; }
  .card--back { top: 478px; }

  .brand {
    position: absolute;
    left: 0; right: 0;
    display: flex;
    align-items: center;
    justify-content: center;
    gap: 12px;
  }
  .brand__dot {
    width: 22px; height: 22px;
    border-radius: 50%;
    background: var(--purple);
  }
  .brand__name {
    font-weight: 700;
    font-size: 58px;
    letter-spacing: -1px;
    color: var(--charcoal);
    line-height: 1;
  }
  .card--front .brand { top: 55px; }
  .card--back .brand { top: 150px; }

  .company-band {
    position: absolute;
    left: 0; right: 0;
    top: 160px; height: 50px;
    background: var(--band-grey);
    display: flex; align-items: center;
    padding-left: 70px;
  }
  .company-band__name {
    font-weight: 700; font-size: 27px; color: var(--charcoal);
  }
  .info-band {
    position: absolute;
    left: 0; right: 0; top: 210px; bottom: 0;
    background: var(--purple-deep);
    color: var(--paper);
  }
  .person {
    position: absolute; left: 70px; bottom: 44px;
  }
  .person__name { font-weight: 700; font-size: 34px; line-height: 1.1; }
  .person__title { font-weight: 500; font-size: 18px; margin-top: 4px; }
  .contact {
    position: absolute; right: 40px; top: 26px;
    list-style: none;
  }
  .contact__item {
    display: flex; align-items: center; gap: 10px;
    font-weight: 500; font-size: 17px; margin-bottom: 8px;
  }
  .contact__icon { width: 18px; height: 18px; flex: none; }

  .back-rule {
    position: absolute; left: 0; right: 0;
    bottom: 72px; height: 10px;
    background: var(--band-grey);
  }
  .back-band {
    position: absolute; left: 0; right: 0;
    bottom: 0; height: 72px;
    background: var(--purple-deep);
  }
</style>
</head>
<body>
  <section class="card card--front">
    <div class="brand">
      <span class="brand__name">brightwell</span>
      <span class="brand__dot"></span>
    </div>
    <div class="company-band">
      <span class="company-band__name">Brightwell Pictures Inc.</span>
    </div>
    <div class="info-band">
      <ul class="contact">
        <li class="contact__item">
          <svg class="contact__icon" viewBox="0 0 18 18" aria-hidden="true">
            <circle cx="9" cy="9" r="9" fill="#fdfdfd"/>
            <path d="M6 4.5l1.6 2.2-1 1.1c.6 1.3 1.5 2.2 2.7 2.8l1.1-1 2.2 1.5-.9 1.7c-3.3-.3-6.1-3.2-6.4-6.5z" fill="#4f2488"/>
          </svg>
          587 914 3362
        </li>
        <li class="contact__item">
          <svg class="contact__icon" viewBox="0 0 18 18" aria-hidden="true">
            <circle cx="9" cy="9" r="9" fill="#fdfdfd"/>
            <rect x="4.5" y="6" width="9" height="6.5" rx="1" fill="#4f2488"/>
            <path d="M4.8 6.4L9 9.6l4.2-3.2" stroke="#fdfdfd" stroke-width="1" fill="none"/>
          </svg>
          mirela@brightwellpix.tv
        </li>
      </ul>
      <div class="person">
        <p class="person__name">Mirela Vantasch</p>
        <p class="person__title">President/Founder</p>
      </div>
    </div>
  </section>

  <section class="card card--back">
    <div class="brand">
      <span class="brand__name">brightwell</span>
      <span class="brand__dot"></span>
    </div>
    <div class="back-rule"></div>
    <div class="back-band"></div>
  </section>
</body>
</html>
```